Heritage Hollow Business Cards

Require a business card design. <br/><br/>Needs to include logo (either round or long version) plus these details:<br/>Maya Torvel<br/>Heritage Hollow<br/>maya@quonbrook.com.au<br/>02 6481 7390<br/>PO Box Glenwarra NSW 2913<br/>www.heritagehollow.com.au<br/><br/>I need in an editable format so that I can create for multiple staff members. <br/><br/>

Target Market(s)

We are an online store selling renovation products to home owners are builders. Looking for a classic classy design.

Industry/Entity Type

Home And Garden

Contact Information for Business Card

Maya Torvel
Heritage Hollow
maya@quonbrook.com.au
02 6481 7390
PO Box Glenwarra NSW 2913
www.heritagehollow.com.au

Colors

Designer to choose colors to be used in the design.

Requirements
Must have
• Must include Logo.

```html
<!DOCTYPE html>
<html lang="en">
<head>
<meta charset="utf-8">
<title>Heritage Hollow Business Cards</title>
<link href="https://fonts.googleapis.com/css2?family=Quattrocento:wght@400;700&family=Roboto:wght@400;500;700&display=swap" rel="stylesheet">
<style>
  :root {
    --bg: #e4e5e8;
    --card-dark: #0b0b0b;
    --card-dark-edge: #1a1a1a;
    --card-light: #ececec;
    --ink: #1c1c1c;
    --ink-soft: #3a3a3a;
    --mark-grey: #5a5a5a;
    --faint: #dcdcdc;
  }
  * { margin: 0; padding: 0; box-sizing: border-box; }
  html, body { width: 1200px; height: 1200px; overflow: hidden; background: var(--bg); }
  .canvas { position: relative; width: 1200px; height: 1200px; }

  .card {
    position: absolute;
    left: 269px;
    width: 663px;
    height: 379px;
    border-radius: 14px;
    overflow: hidden;
  }
  .card--front {
    top: 178px;
    background: radial-gradient(ellipse at 50% 30%, var(--card-dark-edge), var(--card-dark) 70%);
  }
  .card--back { top: 642px; background: var(--card-light); }

  .brand-front {
    position: absolute;
    left: 0; right: 0; top: 196px;
    display: flex; align-items: center; justify-content: center; gap: 14px;
    transform: translateX(-10px);
  }
  .brand-front__dot {
    width: 22px; height: 22px; border-radius: 50%;
    border: 1.5px solid var(--mark-grey);
  }
  .brand-front__name {
    font-family: "Quattrocento", serif;
    font-weight: 700;
    font-size: 44px;
    color: var(--mark-grey);
    letter-spacing: 0.5px;
  }

  .brand-back {
    position: absolute;
    left: 46px; top: 27px;
    width: 160px; height: 160px;
    border-radius: 50%;
    border: 1px solid var(--ink);
    display: flex; align-items: center; justify-content: center;
    text-align: center;
  }
  .brand-back__name {
    font-family: "Quattrocento", serif;
    font-weight: 700;
    font-size: 23px;
    line-height: 1.05;
    color: var(--ink);
  }

  .emblem-faint {
    position: absolute;
    right: 0; top: 0;
    width: 340px; height: 379px;
    background: radial-gradient(ellipse at 80% 55%, var(--faint), rgba(236,236,236,0) 65%);
  }

  .holder {
    position: absolute;
    left: 45px; top: 262px;
    font-family: "Quattrocento", serif;
    font-size: 23px;
    color: var(--ink);
    text-transform: uppercase;
    letter-spacing: 0.3px;
  }
  .company {
    position: absolute;
    left: 45px; top: 310px;
    font-family: "Roboto", sans-serif;
    font-weight: 500;
    font-size: 14px;
    color: var(--ink);
    text-transform: uppercase;
  }
  .contact {
    position: absolute;
    left: 45px;
    font-family: "Roboto", sans-serif;
    font-size: 11.5px;
    color: var(--ink-soft);
    display: flex; align-items: center; gap: 4px;
    white-space: nowrap;
  }
  .contact--address { top: 331px; }
  .contact--lines { top: 349px; }
  .contact svg { width: 10px; height: 10px; fill: var(--ink); flex: none; }
  .contact .sep { margin: 0 6px; }
  .contact strong { font-weight: 700; }
</style>
</head>
<body>
<main class="canvas">

  <section class="card card--front">
    <div class="brand-front">
      <span class="brand-front__dot"></span>
      <span class="brand-front__name">Heritage Hollow</span>
    </div>
  </section>

  <section class="card card--back">
    <div class="emblem-faint" role="img" aria-label="Faint enlarged brand emblem decoration"></div>

    <div class="brand-back">
      <span class="brand-back__name">Heritage<br>Hollow</span>
    </div>

    <h1 class="holder">Maya Torvel</h1>
    <p class="company">Heritage Hollow</p>

    <p class="contact contact--address">
      <svg viewBox="0 0 10 10"><path d="M5 0a3.6 3.6 0 0 0-3.6 3.6C1.4 6.3 5 10 5 10s3.6-3.7 3.6-6.4A3.6 3.6 0 0 0 5 0zm0 5a1.4 1.4 0 1 1 0-2.8A1.4 1.4 0 0 1 5 5z"/></svg>
      PO Box Glenwarra NSW 2913
    </p>

    <p class="contact contact--lines">
      <svg viewBox="0 0 10 10"><path d="M2.1 0.5l1.6 2.1-0.9 1c0.6 1.3 1.6 2.3 2.9 2.9l1-0.9 2.1 1.6-0.8 1.6C5 8.9 1 5 0.5 1.3z"/></svg>
      02 6481 7390
      <span class="sep">|</span>
      <svg viewBox="0 0 10 10"><path d="M0.5 2h9v6h-9zM1 2.5l4 3 4-3" stroke="#fff" stroke-width="0.8"/></svg>
      maya@quonbrook.com.au
      <span class="sep">|</span>
      <svg viewBox="0 0 10 10"><path d="M5 0.5a4.5 4.5 0 1 0 0 9 4.5 4.5 0 0 0 0-9zm0 1c.6.6 1 1.8 1.1 3H3.9C4 3.3 4.4 2.1 5 1.5zM3.9 5.5h2.2C6 6.7 5.6 7.9 5 8.5c-.6-.6-1-1.8-1.1-3zM1.5 4.5c.2-1.2 1-2.2 2-2.7-.3.8-.5 1.7-.6 2.7zm0 1h1.4c.1 1 .3 1.9.6 2.7-1-.5-1.8-1.5-2-2.7zm5.1 2.7c.3-.8.5-1.7.6-2.7h1.4c-.2 1.2-1 2.2-2 2.7zm.6-3.7c-.1-1-.3-1.9-.6-2.7 1 .5 1.8 1.5 2 2.7z"/></svg>
      www.<strong>heritagehollow</strong>.com.au
    </p>
  </section>

</main>
</body>
</html>
```